Ternisa cleaning service in bellevue

we are cleaning service company. We need a brochure to market our service. Its on demand cleaning service. No appointment necessary. Live like a celebrity type of cleaning service. Once they make a call the cleaning is done within in one hour.

Rates: Swift and Stormy $50, Quest Unbeatable $75 and Vanquisher $100

Industry/Entity Type

Cleaning Service

Font styles to use
Decorative
Script

Colors
9bcb3b
3176b5
85cae6
86cfc6
f68d4d

Requirements
Must have
• One call, you can live like a celebrity. Ternisa cleaning service is licensed and bonded, and will arrive prepared with all supplies needed to leave your home looking amazing.
• If you’re not 100% satisfied, money back guaranteed.
• our Logo
Nice to have
• BATHROOMS
• In your bathrooms, we’re going to:
• Dust light fixtures and remove cobwebs
• Remove smudges from cabinets, drawers, doors, and light switches
• Scrub clean the shower, tile, and tub
• Scrub clean the bathroom fixtures
• Hand-wash all mirrors and shower glass
• Scrub clean the toilet
• Remove all trash and reline trash can
• Hand wash all baseboards and floors
• KITCHENS
• Wipe down all counters
• Load breakfast dishes into the dishwasher
• Clean the sink
• Clean the microwave inside and out
• Clean the exterior of the refrigerator, over, and stove top
• Wipe down tables and chairs
• Dust or vacuum baseboards
• Wash floor
• BEDROOMS
• Dust ceiling fans and blinds
• Remove cobwebs
• Wipe down window sills and sashes
• Wipe down and dust picture frames
• Wipe down and dust mirrors
• Tidy up the room
• Make beds with provided sheets
• COMMON LIVING AREAS
• Remove cobwebs
• Smudges removed from doors and light switches
• Dust picture frames and decorations
• Wipe down and dust furniture
• Wipe down exterior of washer and dryer
• Sweep off front porch
• Clean glass on front doors, french doors, and sliding glass doors
• Tidy up where applicable
• Remove all trash and reline trash cans
• Vacuum all carpet and steps
• Vacuum or wash all floors

```html
<!DOCTYPE html>
<html lang="en">
<head>
<meta charset="utf-8">
<title>Ternisa Cleaning Service – Brochure</title>
<link rel="stylesheet" href="https://fonts.googleapis.com/css2?family=Roboto+Condensed:wght@400;700&family=Open+Sans:ital,wght@0,400;0,600;1,700&display=swap">
<style>
:root{
  --board:#a87c55;
  --ink:#1b1b1b;
  --dark-1:#141414;
  --dark-2:#4a4a4a;
  --green:#8cc63f;
  --lime:#9bcb3b;
  --yellow-green:#cddc39;
  --red:#e63c2a;
  --navy:#2b3990;
  --orange:#f68d4d;
  --silver-1:#f4f4f4;
  --silver-2:#a9a9a9;
  --white:#ffffff;
}
*{box-sizing:border-box;margin:0;padding:0}
html,body{width:1200px;height:892px;overflow:hidden}
body{background:var(--board);position:relative;font-family:"Open Sans",Arial,sans-serif;color:var(--ink)}
.side-label{position:absolute;top:52px;font-family:"Times New Roman",Georgia,serif;font-size:26px;font-weight:700;color:var(--white)}
.side-label--back{left:96px}
.side-label--front{left:968px}
.flyer{position:absolute;top:97px;width:510px;height:721px;overflow:hidden;box-shadow:3px 4px 8px rgba(0,0,0,.35);background:var(--dark-1)}
.flyer--back{left:91px}
.flyer--front{left:641px}
.abs{position:absolute}
.dark-band{background:linear-gradient(90deg,var(--dark-1) 0%,#262626 45%,var(--dark-2) 100%)}
.green-band{background:var(--green)}
.cond{font-family:"Roboto Condensed","Arial Narrow",sans-serif;font-weight:700}
.section-title{font-family:"Roboto Condensed","Arial Narrow",sans-serif;font-weight:700;color:var(--red);font-size:19px;letter-spacing:.2px;text-shadow:0 1px 0 rgba(0,0,0,.15)}
.task-list{list-style:none;font-size:7.8px;line-height:1.2;color:var(--ink)}
.task-list li{position:relative;padding-left:13px;margin-bottom:4.6px}
.task-list li::before{content:"";position:absolute;left:0;top:1.5px;width:7px;height:7px;border-radius:50%;background:radial-gradient(circle at 35% 35%,#888,#222)}
.task-list--orange li::before{background:radial-gradient(circle at 35% 35%,#ffc08f,var(--orange))}
.task-list--orange li{margin-bottom:3.8px}
.intro{font-size:9px;font-style:italic;font-weight:700;margin-bottom:7px}
.brand-name{font-family:"Roboto Condensed","Arial Narrow",sans-serif;font-weight:700;color:var(--lime);line-height:1}
.brand-sub{font-family:"Roboto Condensed","Arial Narrow",sans-serif;font-weight:700;color:var(--white);line-height:1}
.footer-bar{left:0;top:671px;width:510px;height:50px;background:linear-gradient(90deg,#3a3a3a,#1a1a1a)}
.contact{position:absolute;left:22px;top:6px;font-family:"Roboto Condensed","Arial Narrow",sans-serif;color:var(--white);font-size:22px}
.contact strong{font-size:29px;font-weight:700;letter-spacing:.5px}
.silver-tab{position:absolute;top:0;right:0;height:50px;background:linear-gradient(180deg,var(--silver-1),#d5d5d5 55%,var(--silver-2))}
/* back */
.price-list{left:272px;top:76px;width:222px}
.price-row{display:flex;justify-content:space-between;color:var(--lime);font-size:20px;line-height:29px}
.price-row .amount{color:var(--yellow-green)}
.col-divider{left:218px;top:203px;width:2px;height:212px;background:#6fa22c}
.notice-box{left:19px;top:415px;width:468px;height:45px;border-radius:3px;background:linear-gradient(180deg,#fff,#e4e4e4);text-align:center}
.notice-box h3{font-family:"Roboto Condensed","Arial Narrow",sans-serif;font-weight:700;color:var(--navy);font-size:20px;line-height:1;margin-top:5px}
.notice-box p{font-size:9px;font-weight:600;color:var(--navy);margin-top:3px}
.slogan{left:14px;top:492px;width:112px;text-align:center;font-family:"Roboto Condensed","Arial Narrow",sans-serif;font-weight:700;line-height:1}
.slogan .lead{color:var(--white);font-size:22px}
.slogan .follow{color:var(--yellow-green);font-size:16px;margin-top:8px;line-height:1.1}
.satisfaction{position:absolute;left:44px;top:16px;font-size:13px;letter-spacing:.5px;color:#333}
.satisfaction::before{content:"";position:absolute;left:-20px;top:3px;width:14px;height:10px;border-radius:50%;background:var(--green)}
/* front */
.tagline{left:20px;top:150px;width:470px;text-align:center;color:var(--white);font-style:italic;font-weight:700;font-size:12.6px;line-height:18px}
.call-out{right:37px;top:20px;text-align:right;font-family:"Roboto Condensed","Arial Narrow",sans-serif;font-weight:700;line-height:1}
.call-out .lead{color:var(--white);font-size:38px}
.call-out .follow{color:var(--yellow-green);font-size:24px;line-height:30px;margin-top:6px}
.guarantee{left:334px;top:515px;width:166px;text-align:center;color:var(--white);font-family:"Roboto Condensed","Arial Narrow",sans-serif;font-weight:700;font-size:21px;line-height:35.5px;text-shadow:0 1px 2px rgba(0,0,0,.3)}
</style>
</head>
<body>
<div class="side-label side-label--back">(Back)</div>
<div class="side-label side-label--front">(Front)</div>

<!-- Back side -->
<section class="flyer flyer--back">
  <div class="abs dark-band" style="left:0;top:0;width:510px;height:203px"></div>
  <svg class="abs" style="left:0;top:0" width="510" height="203" viewBox="0 0 510 203">
    <defs>
      <linearGradient id="floorPhoto" x1="0" y1="0" x2="0" y2="1">
        <stop offset="0" stop-color="#e9e6e1"/><stop offset=".45" stop-color="#b98a63"/><stop offset="1" stop-color="#6b3a1f"/>
      </linearGradient>
      <linearGradient id="rimBack" x1="0" y1="0" x2="1" y2="1">
        <stop offset="0" stop-color="#ffffff"/><stop offset=".5" stop-color="#9a9a9a"/><stop offset="1" stop-color="#e6e6e6"/>
      </linearGradient>
    </defs>
    <path d="M2,38 H322 L350,118 L322,200 H2 Z" fill="url(#rimBack)"/>
    <path d="M2,43 H318 L344,118 L318,195 H2 Z" fill="url(#floorPhoto)" role="img" aria-label="Photo: person vacuuming a polished wooden floor beside an orange sofa"/>
  </svg>
  <div class="abs price-list cond">
    <div class="price-row"><span>Swift and Stormy</span><span class="amount">$50</span></div>
    <div class="price-row"><span>Quest Unbeatable</span><span class="amount">$75</span></div>
    <div class="price-row"><span>Vanquisher</span><span class="amount">$100</span></div>
  </div>

  <div class="abs green-band" style="left:0;top:203px;width:510px;height:262px"></div>
  <div class="abs col-divider"></div>
  <div class="abs" style="left:17px;top:214px;width:196px">
    <h2 class="section-title">BATHROOMS</h2>
    <p class="intro" style="margin-top:9px">In your bathrooms, we’re going to:</p>
    <ul class="task-list">
      <li>Dust light fixtures and remove cobwebs</li>
      <li>Remove smudges from cabinets, drawers, doors, and light switches</li>
      <li>Scrub clean the shower, tile, and tub</li>
      <li>Scrub clean the bathroom fixtures</li>
      <li>Hand-wash all mirrors and shower glass</li>
      <li>Scrub clean the toilet</li>
      <li>Remove all trash and reline trash can</li>
      <li>Hand wash all baseboards and floors</li>
    </ul>
  </div>
  <div class="abs" style="left:231px;top:214px;width:275px">
    <h2 class="section-title">KITCHENS</h2>
    <ul class="task-list" style="margin-top:9px">
      <li>Dust light fixtures and remove cobwebs</li>
      <li>Remove smudges from cabinets, drawers, doors, and light switches</li>
      <li>Wipe down all counters</li>
      <li>Load breakfast dishes into the dishwasher</li>
      <li>Clean the sink</li>
      <li>Clean the microwave inside and out</li>
      <li>Clean the exterior of the refrigerator, over, and stove top</li>
      <li>Wipe down tables and chairs</li>
      <li>Remove all trash and reline trash can</li>
      <li>Dust or vacuum baseboards</li>
      <li>Wash floor</li>
    </ul>
  </div>
  <div class="abs notice-box">
    <h3>No Appointment Necessary</h3>
    <p>Once they make a call the cleaning is done within in one hour.</p>
  </div>

  <div class="abs dark-band" style="left:0;top:465px;width:510px;height:206px"></div>
  <svg class="abs" style="left:0;top:465px" width="510" height="206" viewBox="0 0 510 206">
    <defs>
      <linearGradient id="rimBottom" x1="0" y1="0" x2="0" y2="1">
        <stop offset="0" stop-color="#f5f5f5"/><stop offset="1" stop-color="#8c8c8c"/>
      </linearGradient>
    </defs>
    <path d="M166,3 H510 V170 H166 L140,86 Z" fill="url(#rimBottom)"/>
    <path d="M169,8 H510 V165 H169 L146,86 Z" fill="#8cc63f"/>
  </svg>
  <div class="abs slogan">
    <div class="lead">One Call</div>
    <div class="follow">you can live<br>like a<br>celebrity</div>
  </div>
  <div class="abs" style="left:168px;top:478px">
    <h2 class="section-title">COMMON LIVING AREAS</h2>
  </div>
  <ul class="abs task-list task-list--orange" style="left:170px;top:513px;width:160px">
    <li>Dust ceiling fans and blinds</li>
    <li>Remove cobwebs</li>
    <li>Wipe down window sills and sashes</li>
    <li>Smudges removed from doors and light switches</li>
    <li>Wipe down and dust mirrors</li>
    <li>Dust picture frames and decorations</li>
    <li>Wipe down and dust furniture</li>
  </ul>
  <ul class="abs task-list task-list--orange" style="left:335px;top:513px;width:170px">
    <li>Sweep off front porch</li>
    <li>Clean glass on front doors, french doors, and sliding glass doors</li>
    <li>Tidy up where applicable</li>
    <li>Remove all trash and reline trash cans</li>
    <li>Dust or vacuum baseboards</li>
    <li>Vacuum all carpet and steps</li>
    <li>Vacuum or wash all floors</li>
  </ul>
  <div class="abs" style="left:17px;top:606px">
    <div class="brand-name" style="font-size:48px">Ternisa</div>
    <div class="brand-sub" style="font-size:15px;margin-top:2px">CLEANING SERVICE</div>
  </div>

  <div class="abs footer-bar">
    <div class="contact">Contact: <strong>0198-765-432</strong></div>
    <div class="silver-tab" style="width:197px;clip-path:polygon(17px 0,100% 0,100% 100%,0 100%)">
      <span class="satisfaction">100% SATISFACTION</span>
    </div>
  </div>
</section>

<!-- Front side -->
<section class="flyer flyer--front">
  <div class="abs dark-band" style="left:0;top:0;width:510px;height:203px"></div>
  <div class="abs" style="left:40px;top:36px">
    <div class="brand-name" style="font-size:74px">Ternisa</div>
    <div class="brand-sub" style="font-size:24px;margin-top:2px">CLEANING SERVICE</div>
  </div>
  <div class="abs call-out">
    <div class="lead">One Call</div>
    <div class="follow">you can live like<br>a celebrity</div>
  </div>
  <p class="abs tagline">Ternisa cleaning service is licensed and bonded, and will arrive prepared with all supplies needed to leave your home looking amazing.</p>

  <div class="abs" role="img" aria-label="Photo: person vacuuming a cream shag carpet in a bright living room" style="left:0;top:203px;width:510px;height:262px;background:linear-gradient(160deg,#f6f4f0 0%,#e8e1d6 45%,#d7ccbb 100%)"></div>
  <div class="abs" style="left:27px;top:294px;width:200px">
    <h2 class="section-title">BEDROOMS</h2>
    <ul class="task-list" style="margin-top:10px">
      <li>Dust ceiling fans and blinds</li>
      <li>Remove cobwebs</li>
      <li>Wipe down window sills and sashes</li>
      <li>Wipe down and dust picture frames</li>
      <li>Wipe down and dust mirrors</li>
      <li>Tidy up the room</li>
      <li>Make beds with provided sheets</li>
      <li>Remove all trash and reline trash can</li>
      <li>Dust or vacuum baseboards</li>
    </ul>
  </div>

  <div class="abs green-band" style="left:0;top:465px;width:510px;height:206px"></div>
  <div class="abs" role="img" aria-label="Photo: cleaner in green gloves scrubbing a white bathtub with red tiles" style="left:25px;top:473px;width:309px;height:175px;border:2px solid #fff;background:linear-gradient(180deg,#e0554a 0%,#f0d9d2 45%,#ffffff 70%,#eaeaea 100%)"></div>
  <div class="abs guarantee">IF YOU’RE NOT<br>100% SATISFIED<br>MONEY BACK<br>GUARANTEED</div>

  <div class="abs footer-bar">
    <div class="contact">Contact: <strong>0198-765-432</strong></div>
    <div class="abs" style="left:308px;top:0;width:24px;height:50px;background:var(--green);clip-path:polygon(12px 0,100% 0,12px 100%,0 100%)"></div>
    <div class="silver-tab" style="width:190px;clip-path:polygon(12px 0,100% 0,100% 100%,0 100%)">
      <div style="position:absolute;left:52px;top:4px;text-align:center">
        <div class="brand-name" style="font-size:28px;color:var(--green)">Ternisa</div>
        <div class="cond" style="font-size:9px;color:var(--navy);line-height:1;margin-top:1px">CLEANING SERVICE</div>
      </div>
    </div>
  </div>
</section>
</body>
</html>
```